Sci fi cover needed for Brimbly/aMolder

I'd like a variation on the below design, I like the white logo with the colour blending in but this time with a different colour and different graphic below. No subtitle needed.

```html
<!DOCTYPE html>
<html lang="en">
<head>
<meta charset="utf-8">
<title>Outland Starside Depot</title>
<link rel="stylesheet" href="https://fonts.googleapis.com/css2?family=Black+Ops+One&display=swap">
<style>
  :root {
    --bg-top: #0c0604;
    --bg-mid: #1c0c06;
    --bg-bottom: #2e1206;
    --title-white: #ffffff;
    --title-warm: #ffe2b8;
    --title-amber: #ffa21f;
    --glow-core: #ffc35a;
    --glow-deep: #d8520a;
  }
  html, body {
    margin: 0;
    padding: 0;
    width: 1200px;
    height: 1200px;
    overflow: hidden;
    background: var(--bg-top);
  }
  .cover {
    position: relative;
    width: 1200px;
    height: 1200px;
    overflow: hidden;
    background: linear-gradient(180deg, var(--bg-top) 0%, var(--bg-mid) 55%, var(--bg-bottom) 100%);
    font-family: "Black Ops One", "Arial Black", sans-serif;
  }
  .title-art {
    position: absolute;
    left: 0;
    top: 0;
    width: 1200px;
    height: 440px;
  }
  .title-art text {
    font-family: "Black Ops One", "Arial Black", sans-serif;
  }
  .planet-art {
    position: absolute;
    left: 200px;
    top: 500px;
    width: 800px;
    height: 660px;
    background:
      radial-gradient(circle at 50% 52%, rgba(255, 195, 90, 0.85) 0%, rgba(255, 162, 31, 0.55) 22%, rgba(216, 82, 10, 0.35) 38%, transparent 46%),
      radial-gradient(ellipse 48% 8% at 50% 55%, rgba(255, 210, 140, 0.5) 0%, rgba(216, 82, 10, 0.25) 60%, transparent 90%),
      radial-gradient(ellipse 60% 55% at 50% 55%, rgba(216, 82, 10, 0.3) 0%, transparent 80%);
  }
</style>
</head>
<body>
  <main class="cover">
    <svg class="title-art" viewBox="0 0 1200 440" xmlns="http://www.w3.org/2000/svg">
      <defs>
        <linearGradient id="title-fade" gradientUnits="userSpaceOnUse" x1="0" y1="88" x2="0" y2="392">
          <stop offset="0" stop-color="var(--title-white)" />
          <stop offset="0.45" stop-color="var(--title-white)" />
          <stop offset="0.68" stop-color="var(--title-warm)" />
          <stop offset="1" stop-color="var(--title-amber)" />
        </linearGradient>
      </defs>
      <text class="title-main" x="185" y="280" font-size="272" textLength="826" lengthAdjust="spacingAndGlyphs" fill="url(#title-fade)">OUTLAND</text>
      <text class="title-sub" x="185" y="390" font-size="132" textLength="826" lengthAdjust="spacingAndGlyphs" fill="url(#title-fade)">STARSIDEDEPOT</text>
    </svg>
    <div class="planet-art" role="img" aria-label="Glowing amber planet with a bright ring of light hanging in deep space"></div>
  </main>
</body>
</html>
```